Selam-Kaveh - Promote and Support a community

Design a website for Ethiopean Community. the design should be friendly, easy to navigate and maintain the look & feel of the Ethiopian culture. a proposed logo is attached but it can be change according to your recommendations. This is a project we are doing at a discount rate as it supports a weak community.
Please visit their current website http://www.selam-kaveh.example.org/index.php?lang=en

Target Market(s)

Community members, potential doners

Industry/Entity Type

community

Number of Pages Required

1 page

Font styles to use
Sans Serif

Requirements
Must have
• easy to navigate friendly interface

```html
<!DOCTYPE html>
<html lang="en">
<head>
<meta charset="utf-8">
<title>Selam-Kaveh</title>
<link href="https://fonts.googleapis.com/css2?family=League+Spartan:wght@500;600;700&family=Jost:wght@300;400;500&display=swap" rel="stylesheet">
<style>
:root{
  --red:#8c0f22;
  --yellow:#f6e27f;
  --navy:#1f3e4e;
  --ink:#1c2b33;
  --text:#5f666b;
  --sky:#bfe0e9;
  --foot:#f6f6f6;
}
*{margin:0;padding:0;box-sizing:border-box}
html,body{width:1200px;height:3937px;overflow:hidden}
body{position:relative;font-family:"Jost",sans-serif;color:var(--text);background:#fff}
.abs{position:absolute}
h1,h2,h3,h4,.brand{font-family:"League Spartan",sans-serif;color:var(--ink)}
.btn{position:absolute;display:flex;align-items:center;justify-content:center;gap:8px;background:var(--yellow);color:var(--ink);font:500 13px "League Spartan",sans-serif;text-decoration:none}
.btn svg{width:13px;height:13px}
.eyebrow{font-size:14px;letter-spacing:.5px;text-transform:uppercase;color:#4f5a60}
.heading{font-size:34px;font-weight:700;line-height:41px}
.para{font-size:17px;line-height:27px;font-weight:300}

/* header */
.topbar{top:0;left:0;width:1200px;height:87px;background:#fff}
.brand{left:168px;top:22px;display:flex;align-items:center;gap:12px;font-size:24px;font-weight:700;color:#2e4f3f}
.brand i{display:block;width:42px;height:42px;border-radius:50%;background:var(--red)}
.contact{display:flex;align-items:center;gap:12px;font-size:12.5px;color:var(--ink);line-height:17px}
.contact .ic{width:44px;height:44px;border-radius:50%;background:var(--yellow);display:flex;align-items:center;justify-content:center}
.lang{left:925px;top:26px;width:115px;height:35px;background:var(--navy);color:#fff;font:500 13px "League Spartan",sans-serif;display:flex;align-items:center;justify-content:center;gap:7px}
.nav{top:87px;left:0;width:1200px;height:45px;background:var(--red);display:flex;justify-content:center;align-items:center}
.nav a{color:#fff;font:600 13px "League Spartan",sans-serif;text-decoration:none;padding:0 16px;border-left:1px solid rgba(255,255,255,.8);line-height:12px}
.nav a:first-child{border-left:none}

/* hero */
.hero{top:132px;left:0;width:1200px;height:443px;background:radial-gradient(circle at 600px 340px,#6a3a8a 0,#c43a4a 18%,#d99a2a 35%,#3f8a6a 55%,#b53050 75%,#e0b030 100%)}
.hero::after{content:"";position:absolute;inset:0;background:rgba(40,10,20,.35)}
.hero-copy{position:absolute;z-index:1;left:0;width:1200px;text-align:center;color:#fff}
.hero .arrow{position:absolute;z-index:1;top:148px;width:54px;height:54px;border-radius:50%;background:rgba(255,255,255,.25);display:flex;align-items:center;justify-content:center}

/* about */
.photo{position:absolute}
.about-img{left:159px;top:638px;width:419px;height:351px;border-radius:90px 0 0 70px;background:linear-gradient(135deg,#e8b070 0%,#d2542e 45%,#a03030 70%,#8a6c50 100%);box-shadow:6px 6px 0 var(--red)}

/* community */
.community{top:1050px;left:0;width:1200px;height:540px;background:var(--sky)}
.ring1{left:617px;top:1112px;width:425px;height:425px;border-radius:50%;background:#d2eaf0}
.ring2{left:640px;top:1135px;width:380px;height:380px;border-radius:50%;background:#e6f3f6}
.comm-img{left:661px;top:1156px;width:338px;height:338px;border-radius:50%;background:radial-gradient(circle at 50% 40%,#b07850,#5a3420 60%,#efefef 100%)}

/* programs */
.card{position:absolute;top:1748px;width:281px;height:341px;border:2px solid #c9d3d8;padding:5px}
.card .inner{width:100%;height:100%;box-shadow:0 0 0 1px #e3e8ea;text-align:center;padding-top:36px}
.card.feature .inner{background:var(--yellow)}
.card h3{font-size:20px;font-weight:600;line-height:27px;margin-top:20px}
.card .rule{width:60px;height:2px;background:var(--red);margin:10px auto 12px}
.card p{font-size:16px;line-height:27px;font-weight:300;padding:0 22px;color:#555}
.card .more{margin-top:18px;display:flex;justify-content:center;align-items:center;gap:7px;font:600 12.5px "League Spartan",sans-serif;color:var(--ink)}

/* advocacy */
.advocacy{top:2226px;left:0;width:1200px;height:461px;background:linear-gradient(90deg,#2c4555 0%,#324b5a 55%,#45535a 80%,#3a4952 100%)}
.adv-img{left:159px;top:2289px;width:419px;height:333px;border-radius:60px 0 0 60px;background:linear-gradient(135deg,#8a6a4a,#4a3a30 40%,#e8a0a0 70%,#2a2222)}

/* news */
.date{position:absolute;background:var(--yellow);color:var(--ink);font:600 16px/17px "League Spartan",sans-serif;text-align:center}
.news-title{font:600 15.5px/26px "League Spartan",sans-serif;color:var(--ink)}
.news-more{font:600 12.5px "League Spartan",sans-serif;color:var(--ink);display:flex;align-items:center;gap:7px}

/* support */
.support{top:3244px;left:0;width:1200px;height:355px;background:linear-gradient(90deg,#22384a,#2d4559 50%,#22384a)}

/* footer */
.footer{top:3599px;left:0;width:1200px;height:338px;background:var(--foot)}
.footer h4{font-size:20px;font-weight:700}
.flinks{font-size:15.5px;line-height:29px;font-weight:300;color:#555}
.fcontact{display:flex;gap:16px;font-size:15.5px;line-height:21px;font-weight:300;color:#555}
.fcontact svg{flex:none;margin-top:4px}
.social{display:flex;gap:12px}
.social span{width:12px;height:12px;border-radius:50%;background:var(--ink)}
</style>
</head>
<body>

<header class="abs topbar">
  <div class="abs brand"><i></i>Selam Kaveh</div>
  <div class="abs contact" style="left:464px;top:21px">
    <div class="ic"><svg width="22" height="16" viewBox="0 0 22 16" fill="none" stroke="#1c2b33" stroke-width="1.5"><rect x="1" y="1" width="20" height="14" rx="2"/><path d="M1 2l10 7 10-7"/></svg></div>
    <div>Email:<br>selamkaveh@example.org</div>
  </div>
  <div class="abs contact" style="left:713px;top:21px">
    <div class="ic"><svg width="20" height="20" viewBox="0 0 24 24" fill="none" stroke="#1c2b33" stroke-width="1.5"><path d="M5 3h4l2 5-3 2a11 11 0 006 6l2-3 5 2v4a2 2 0 01-2 2A17 17 0 013 5a2 2 0 012-2z"/></svg></div>
    <div>Phone:<br>04-5550137</div>
  </div>
  <div class="abs lang">
    <svg width="13" height="13" viewBox="0 0 24 24" fill="none" stroke="#fff" stroke-width="2"><circle cx="12" cy="12" r="10"/><path d="M2 12h20M12 2c3 3 3 17 0 20M12 2c-3 3-3 17 0 20"/></svg>
    English
    <svg width="9" height="9" viewBox="0 0 10 10"><path d="M1 3l4 4 4-4" stroke="#fff" stroke-width="2" fill="none"/></svg>
  </div>
</header>
<nav class="abs nav">
  <a>Home</a><a>About</a><a>The Community</a><a>Programs</a><a>News</a><a>Advocacy</a><a>Partners</a><a>Support Us</a><a>Contact Us</a>
</nav>

<section class="abs hero" role="img" aria-label="Photo of colourful woven Ethiopian baskets">
  <div class="arrow" style="left:95px"><svg width="14" height="20" viewBox="0 0 14 20"><path d="M10 3L3 10l7 7" stroke="#fff" stroke-width="2" fill="none"/></svg></div>
  <div class="arrow" style="left:1049px"><svg width="14" height="20" viewBox="0 0 14 20"><path d="M4 3l7 7-7 7" stroke="#fff" stroke-width="2" fill="none"/></svg></div>
  <div class="hero-copy" style="top:52px;font-size:28px;letter-spacing:2px;font-weight:300">WELCOME TO</div>
  <div class="hero-copy" style="top:84px;font:700 78px/86px 'League Spartan',sans-serif;color:#fff">Selam-Kaveh</div>
  <div class="hero-copy" style="top:164px;font-size:16px;line-height:24px;font-weight:300">Selam Kaveh was founded in 1999 by Dr. Miriam<br>Halevi, Head of the Endocrinology Unit at the<br>Carmel Valley Medical Center.</div>
  <a class="btn" style="left:530px;top:256px;width:138px;height:39px;z-index:1">Contact Us <svg viewBox="0 0 16 16"><circle cx="8" cy="8" r="8" fill="#1c2b33"/><path d="M6 4l4 4-4 4" stroke="#f6e27f" stroke-width="2" fill="none"/></svg></a>
</section>

<section>
  <div class="photo about-img" role="img" aria-label="Photo of a smiling Ethiopian family outdoors"></div>
  <div class="abs eyebrow" style="left:610px;top:651px">About Us</div>
  <h2 class="abs heading" style="left:610px;top:673px">Welcome to Selam Kaveh</h2>
  <p class="abs para" style="left:610px;top:719px;width:420px">Aliyah (immigration) from Ethiopia to Israel and the transition to a sedentary lifestyle has resulted in the emergence of chronic diseases, in particular diabetes. While only 0.4% of the new immigrants were diagnosed with Type 2 diabetes upon arrival, by the time they had lived in Israel for ten years the figure had risen to 18% - three times as many as in the general population.</p>
  <a class="btn" style="left:610px;top:933px;width:155px;height:37px">More About Us <svg viewBox="0 0 16 16"><circle cx="8" cy="8" r="8" fill="#1c2b33"/><path d="M6 4l4 4-4 4" stroke="#f6e27f" stroke-width="2" fill="none"/></svg></a>
</section>

<section class="abs community"></section>
<div class="abs ring1"></div>
<div class="abs ring2"></div>
<div class="photo comm-img" role="img" aria-label="Photo of a mother holding her young son"></div>
<div class="abs eyebrow" style="left:159px;top:1150px">The Community</div>
<h2 class="abs heading" style="left:159px;top:1172px;width:420px">Health &amp; the Ethiopian Israeli Community</h2>
<p class="abs para" style="left:159px;top:1265px;width:415px">Today the Ethiopian Israeli community numbers over 120,000 with new immigrants still continuing to arrive. For many, immigration led to the disintegration of traditional family and social structures with traumatic results for the community and further impeding absorption into Israeli society.</p>
<a class="btn" style="left:159px;top:1450px;width:200px;height:36px">Go To The Community <svg viewBox="0 0 16 16"><circle cx="8" cy="8" r="8" fill="#1c2b33"/><path d="M6 4l4 4-4 4" stroke="#f6e27f" stroke-width="2" fill="none"/></svg></a>

<div class="abs eyebrow" style="left:0;width:1200px;text-align:center;top:1650px">Services</div>
<h2 class="abs heading" style="left:0;width:1200px;text-align:center;top:1672px">Our Programs</h2>

<div class="card" style="left:159px"><div class="inner">
  <svg width="66" height="56" viewBox="0 0 66 56" fill="none" stroke="#1c2b33" stroke-width="1.6"><rect x="22" y="3" width="40" height="30"/><circle cx="42" cy="17" r="7"/><path d="M42 13v8M38 17h8"/><circle cx="12" cy="30" r="5"/><path d="M4 53v-10a8 8 0 0116 0v10M20 40l10-8"/><circle cx="34" cy="40" r="4"/><circle cx="48" cy="40" r="4"/><path d="M27 53a7 7 0 0114 0M41 53a7 7 0 0114 0"/></svg>
  <h3>Health &amp; Education<br>Presentations</h3><div class="rule"></div>
  <p>To spread awareness of a health promoting lifestyle &amp; an understanding of..</p>
  <div class="more">Read More <svg width="13" height="13" viewBox="0 0 16 16"><circle cx="8" cy="8" r="8" fill="#1c2b33"/><path d="M6 4l4 4-4 4" stroke="#fff" stroke-width="2" fill="none"/></svg></div>
</div></div>

<div class="card feature" style="left:459px"><div class="inner">
  <svg width="60" height="56" viewBox="0 0 60 56" fill="none" stroke="#1c2b33" stroke-width="1.6"><rect x="3" y="16" width="54" height="36" rx="6"/><path d="M14 16l30-12"/><rect x="10" y="23" width="40" height="8" rx="2"/><circle cx="40" cy="42" r="5"/><circle cx="28" cy="42" r="3"/><path d="M12 38h8M12 44h8"/></svg>
  <h3>Amharic Radio<br>Program</h3><div class="rule"></div>
  <p>To reach the widest possible audience Selam Kaveh produces a fortnightly radio..</p>
  <div class="more">Read More <svg width="13" height="13" viewBox="0 0 16 16"><circle cx="8" cy="8" r="8" fill="#1c2b33"/><path d="M6 4l4 4-4 4" stroke="#f6e27f" stroke-width="2" fill="none"/></svg></div>
</div></div>

<div class="card" style="left:760px"><div class="inner">
  <svg width="56" height="60" viewBox="0 0 56 60" fill="none" stroke="#1c2b33" stroke-width="1.6"><path d="M20 58V44l-6-10V22a3 3 0 016 0v8-14a3 3 0 016 0v14-16a3 3 0 016 0v16-12a3 3 0 016 0v20l-4 10v12z"/><path d="M28 2v5M14 6l3 4M42 6l-3 4M8 16h4M44 16h4"/></svg>
  <h3>Health Leadership<br>Development</h3><div class="rule"></div>
  <p>In partnership with Dr. Daniel Orbach of Bridging Care Network and Briut Plus..</p>
  <div class="more">Read More <svg width="13" height="13" viewBox="0 0 16 16"><circle cx="8" cy="8" r="8" fill="#1c2b33"/><path d="M6 4l4 4-4 4" stroke="#fff" stroke-width="2" fill="none"/></svg></div>
</div></div>

<a class="btn" style="left:515px;top:2125px;width:170px;height:39px;background:var(--navy);color:#fff">View All Services <svg viewBox="0 0 16 16"><circle cx="8" cy="8" r="8" fill="#fff"/><path d="M6 4l4 4-4 4" stroke="#1f3e4e" stroke-width="2" fill="none"/></svg></a>

<section class="abs advocacy" role="img" aria-label="Dimmed background photo of a smiling woman"></section>
<div class="photo adv-img" role="img" aria-label="Photo of a group of community members in a law library"></div>
<div class="abs eyebrow" style="left:610px;top:2318px;color:#d9e1e5">Advocacy</div>
<h2 class="abs heading" style="left:608px;top:2340px;color:#fff">Need Advocacy</h2>
<p class="abs para" style="left:610px;top:2392px;width:435px;color:#d9e1e5">To advocate the unique needs of the community Selam Kaveh urges members of the national assembly, the ministries for health, welfare and integration, and the Civic Welfare Fund (Keren Ezra) to adopt measures that will improve the circumstances.</p>
<a class="btn" style="left:610px;top:2552px;width:130px;height:38px">View More <svg viewBox="0 0 16 16"><circle cx="8" cy="8" r="8" fill="#1c2b33"/><path d="M6 4l4 4-4 4" stroke="#f6e27f" stroke-width="2" fill="none"/></svg></a>

<div class="abs eyebrow" style="left:0;width:1200px;text-align:center;top:2745px">Blog</div>
<h2 class="abs heading" style="left:0;width:1200px;text-align:center;top:2767px">Latest News</h2>

<div class="photo" style="left:159px;top:2835px;width:431px;height:275px;background:linear-gradient(135deg,#5a4a3a,#8a7a60 40%,#3e5a3a 70%,#6a5a4a)" role="img" aria-label="Photo of a large group of community members"></div>
<div class="date" style="left:159px;top:2835px;width:65px;height:65px;padding-top:14px">12<br>Jan</div>
<div class="abs news-title" style="left:159px;top:3131px;width:420px">It is a long established fact that a reader will be distracted by the readable</div>

<div class="photo" style="left:610px;top:2835px;width:205px;height:163px;background:linear-gradient(135deg,#3a2418,#8a5a3a 50%,#2a1a12)" role="img" aria-label="Photo of joined hands in a circle"></div>
<div class="date" style="left:610px;top:2835px;width:58px;height:62px;padding-top:14px">22<br>Feb</div>
<div class="abs news-title" style="left:833px;top:2846px;width:210px">It is a long established fact tracted by the readable</div>
<p class="abs para" style="left:833px;top:2901px;width:215px;font-size:15.5px">There are many variations of passages of Lorem Ipsum</p>
<div class="abs news-more" style="left:833px;top:2968px">Read More <svg width="13" height="13" viewBox="0 0 16 16"><circle cx="8" cy="8" r="8" fill="#1c2b33"/><path d="M6 4l4 4-4 4" stroke="#fff" stroke-width="2" fill="none"/></svg></div>

<div class="photo" style="left:610px;top:3017px;width:205px;height:165px;background:linear-gradient(160deg,#c9d8a0,#7a9a5a 45%,#b5653a 80%)" role="img" aria-label="Photo of a mother and child walking on a dirt road"></div>
<div class="date" style="left:610px;top:3017px;width:58px;height:62px;padding-top:14px">30<br>Oct</div>
<div class="abs news-title" style="left:833px;top:3028px;width:210px">It is a long established fact tracted by the readable</div>
<p class="abs para" style="left:833px;top:3083px;width:215px;font-size:15.5px">There are many variations of passages of Lorem Ipsum</p>
<div class="abs news-more" style="left:833px;top:3150px">Read More <svg width="13" height="13" viewBox="0 0 16 16"><circle cx="8" cy="8" r="8" fill="#1c2b33"/><path d="M6 4l4 4-4 4" stroke="#fff" stroke-width="2" fill="none"/></svg></div>

<section class="abs support" role="img" aria-label="Dimmed background photo of community volunteers"></section>
<h2 class="abs heading" style="left:0;width:1200px;text-align:center;top:3334px;color:#fff">Support Us</h2>
<p class="abs para" style="left:0;width:1200px;text-align:center;top:3387px;color:#fff;font-weight:400;font-size:16px">Selam Kaveh non-profit organization operates to promote the ethiopian israel<br>community healthcare, using donations and govermant funding.</p>
<a class="btn" style="left:427px;top:3466px;width:347px;height:36px">For donation via credit card please click here <svg viewBox="0 0 16 16"><circle cx="8" cy="8" r="8" fill="#1c2b33"/><path d="M6 4l4 4-4 4" stroke="#f6e27f" stroke-width="2" fill="none"/></svg></a>

<footer class="abs footer">
  <h4 class="abs" style="left:159px;top:45px">About Us</h4>
  <p class="abs flinks" style="left:159px;top:74px;width:320px">Selam Kaveh ("peace" in Amharic) is dedicated to improving the health of the Ethiopian Israeli community.</p>
  <a class="btn" style="left:159px;top:166px;width:131px;height:36px">View More <svg viewBox="0 0 16 16"><circle cx="8" cy="8" r="8" fill="#1c2b33"/><path d="M6 4l4 4-4 4" stroke="#f6e27f" stroke-width="2" fill="none"/></svg></a>
  <div class="abs social" style="left:159px;top:225px" aria-label="Social links"><span></span><span></span><span></span><span></span></div>

  <h4 class="abs" style="left:512px;top:45px">Quick Links</h4>
  <div class="abs flinks" style="left:512px;top:73px">Home<br>About<br>The Community<br>Programs<br>News</div>
  <div class="abs flinks" style="left:665px;top:73px">Advocacy<br>Partners<br>Support Us<br>Contact Us</div>

  <h4 class="abs" style="left:833px;top:45px">Contact Us</h4>
  <div class="abs fcontact" style="left:833px;top:78px"><svg width="13" height="16" viewBox="0 0 12 16"><path d="M6 0a6 6 0 016 6c0 4-6 10-6 10S0 10 0 6a6 6 0 016-6z" fill="#1c2b33"/><circle cx="6" cy="6" r="2" fill="#f6f6f6"/></svg><div>Tsion 12/4 POB 4410<br>Netanya, 40200</div></div>
  <div class="abs fcontact" style="left:833px;top:136px"><svg width="14" height="14" viewBox="0 0 24 24"><path d="M5 2h4l2 6-3 2a12 12 0 006 6l2-3 6 2v4a3 3 0 01-3 3A19 19 0 012 5a3 3 0 013-3z" fill="#1c2b33"/></svg><div>Phone:<br>04-5550137</div></div>
  <div class="abs fcontact" style="left:833px;top:190px"><svg width="14" height="12" viewBox="0 0 14 11"><rect width="14" height="11" rx="1" fill="#1c2b33"/><path d="M0 1l7 5 7-5" stroke="#f6f6f6" fill="none"/></svg><div>Email:<br>selamkaveh@example.org</div></div>

  <p class="abs" style="left:0;width:1200px;text-align:center;top:290px;font-size:14px;font-weight:300;color:#777">Copyright © 2022 Selam Kaveh. All rights reserved.</p>
</footer>

</body>
</html>
```